Make my current Presentation more Professional

I am selling frozen pulp and sorbets. I have a presentation done to introduce the product to customers i want to sell my product to. However the presentation does not have a character - i need to make it look more professional, and at the same time i want to make the product stand out, and have the overall presentation look very fresh, and embedding the true look and feel of what we are offering. 100% NATURAL TROPICAL BRAZILIAN FRUITS.
Some of the text in the presentation is pasted like image, i need it as text.
There should be a specific template that you will use so that i can add remove slides later on according to my requirement

Target Market(s)

Presentation is intended for F&B managers & Chefs in hotels, restaurant

Industry/Entity Type

Food Service

Font styles to use
Sans Serif

Colors

Designer to choose colors to be used in the design.

Requirements
Must have
• A fresh, natural look and feel of tropical fruits.
• It also should come across professional as we are selling products to potential customers.
• I need a clear template - with header, font etc..
Nice to have
• If you want to buy some pictures of fruits, i can buy it for you to make it look great

```html
<!DOCTYPE html>
<html lang="en">
<head>
<meta charset="UTF-8">
<title>Our Products</title>
<link rel="stylesheet" href="https://fonts.googleapis.com/css2?family=Poppins:wght@500;600&display=swap">
<style>
  :root {
    --bg-top: #f7f9f1;
    --bg-bottom: #eef4e2;
    --lime: #86bc1d;
    --leaf: #3f9a3a;
    --mango: #f5a623;
    --brand-green: #1f7a2e;
  }
  * { margin: 0; padding: 0; box-sizing: border-box; }
  html, body { width: 1200px; height: 675px; overflow: hidden; background: var(--bg-top); }
  .slide {
    position: relative;
    width: 1200px;
    height: 675px;
    background: linear-gradient(180deg, var(--bg-top) 0%, var(--bg-bottom) 100%);
    font-family: "Poppins", sans-serif;
    color: var(--lime);
  }
  .slide-title {
    position: absolute;
    top: 112px;
    left: 0;
    width: 100%;
    text-align: center;
    font-size: 48px;
    font-weight: 600;
    line-height: 60px;
    letter-spacing: -0.5px;
  }
  .product {
    position: absolute;
    top: 272px;
    width: 360px;
    margin-left: -180px;
    display: flex;
    flex-direction: column;
    align-items: center;
  }
  .product--pulps { left: 273px; }
  .product--sorbets { left: 616px; }
  .product--smoothies { left: 937px; }
  .product-icon { width: 160px; height: 160px; display: block; }
  .product-name {
    margin-top: 22px;
    font-size: 29px;
    font-weight: 500;
    line-height: 40px;
    text-align: center;
  }
  .brand {
    position: absolute;
    left: 0;
    bottom: 24px;
    width: 100%;
    display: flex;
    justify-content: center;
    align-items: center;
    gap: 8px;
  }
  .brand-dot {
    width: 26px;
    height: 26px;
    border-radius: 50%;
    background: var(--brand-green);
  }
  .brand-name {
    font-family: "Poppins", sans-serif;
    font-size: 22px;
    font-weight: 600;
    color: var(--brand-green);
  }
</style>
</head>
<body>
<main class="slide">
  <h1 class="slide-title">Our Products</h1>

  <section class="product product--pulps">
    <svg class="product-icon" viewBox="-80 -80 160 160" aria-hidden="true">
      <g fill="none" stroke-linejoin="round" stroke-linecap="round">
        <circle r="67" stroke="var(--leaf)" stroke-width="7"/>
        <circle r="54" stroke="var(--lime)" stroke-width="5"/>
        <g stroke="var(--mango)" stroke-width="4.5">
          <path id="wedge" d="M0 -9 L-13 -41 A43 43 0 0 1 13 -41 Z"/>
          <use href="#wedge" transform="rotate(45)"/>
          <use href="#wedge" transform="rotate(90)"/>
          <use href="#wedge" transform="rotate(135)"/>
          <use href="#wedge" transform="rotate(180)"/>
          <use href="#wedge" transform="rotate(225)"/>
          <use href="#wedge" transform="rotate(270)"/>
          <use href="#wedge" transform="rotate(315)"/>
        </g>
      </g>
    </svg>
    <h2 class="product-name">Pulps<br>Variety</h2>
  </section>

  <section class="product product--sorbets">
    <svg class="product-icon" viewBox="-80 -8 160 160" aria-hidden="true">
      <g fill="none" stroke-width="5" stroke-linejoin="round">
        <rect x="-31" y="0" width="62" height="99" rx="11" stroke="var(--leaf)"/>
        <path d="M-10 99 V140 A10 10 0 0 0 10 140 V99" stroke="var(--mango)"/>
        <rect x="-17" y="17" width="10" height="66" rx="5" stroke="var(--lime)"/>
        <rect x="7" y="17" width="10" height="66" rx="5" stroke="var(--lime)"/>
      </g>
    </svg>
    <h2 class="product-name">Sorbetti/Vitaminas<br>Acai Na Tejela</h2>
  </section>

  <section class="product product--smoothies">
    <svg class="product-icon" viewBox="-80 -8 160 160" aria-hidden="true">
      <g fill="none" stroke-width="5" stroke-linejoin="round" stroke-linecap="round">
        <path d="M-38 64 A38 32 0 0 1 38 64" stroke="var(--lime)"/>
        <rect x="-40" y="64" width="80" height="10" rx="4" stroke="var(--leaf)"/>
        <path d="M-35 74 L-29 145 H29 L35 74" stroke="var(--leaf)"/>
        <path d="M8 38 L22 10 L38 2" stroke="var(--mango)"/>
      </g>
    </svg>
    <h2 class="product-name">Smoothies</h2>
  </section>

  <footer class="brand">
    <span class="brand-dot"></span>
    <span class="brand-name">Polpa Viva</span>
  </footer>
</main>
</body>
</html>
```